Swift Horizon Ride (SH Ride) Needs a flyer designed

We need a flyer designed to pass out around town that showcases our awesome "high end" indoor cycle/spin classes that are held at our gym (called BoltForge Millbrook Vale). Please visit our website to get a better idea of what we do. www.boltForgemv.com.
"Our team at BoltForge Millbrook Vale is proud to offer challenging and exciting indoor Cycling classes. Swift Horizon Ride consist of state of the art bikes, awesome lighting, performance fitness software and much MORE! All this is done through a fast paced, high intensity cycling class taught by Rancho’s best instructors. We even track your individual performance for each class so you know you’re getting FITTER!"
Flyer should:
1) Double sided
2) contain location (refer to website)
3) a "try us for FREE"
4) anything else you think is needed
Town

```html
<!DOCTYPE html>
<html lang="en">
<head>
<meta charset="utf-8">
<title>Swift Horizon Ride – Indoor Cycling Flyer</title>
<link href="https://fonts.googleapis.com/css2?family=Roboto+Condensed:ital,wght@0,700;0,800;1,800&display=swap" rel="stylesheet">
<style>
  :root {
    --black: #050505;
    --red: #e3120f;
    --red-bright: #ff1a12;
    --red-mid: #c50c0c;
    --red-deep: #7a0507;
    --red-dark: #3a0204;
    --band-grey: #3d3d3d;
    --band-dark: #1c1c1c;
    --white: #ffffff;
  }
  html, body {
    margin: 0;
    padding: 0;
    width: 811px;
    height: 1200px;
    overflow: hidden;
    background: var(--black);
  }
  .flyer {
    position: relative;
    width: 811px;
    height: 1200px;
    overflow: hidden;
    font-family: "Roboto Condensed", "Arial Narrow", sans-serif;
    background:
      radial-gradient(ellipse 60% 40% at 0% 50%, var(--red-deep) 0%, rgba(122,5,7,0) 100%),
      linear-gradient(180deg, var(--black) 0%, #120102 35%, var(--red-dark) 100%);
  }
  .brand {
    position: absolute;
    top: 110px;
    left: 0;
    width: 811px;
    display: flex;
    justify-content: center;
    align-items: center;
    gap: 14px;
  }
  .brand-mark {
    width: 22px;
    height: 22px;
    background: var(--red);
  }
  .brand-name {
    color: var(--white);
    font-weight: 800;
    font-size: 42px;
    line-height: 1;
  }
  .band {
    position: absolute;
    inset: 0;
    background:
      radial-gradient(ellipse 50% 60% at 75% 35%, #4a4a4a 0%, rgba(74,74,74,0) 100%),
      linear-gradient(200deg, var(--band-grey) 0%, #2a2a2a 45%, var(--band-dark) 100%);
    clip-path: polygon(0 395px, 811px 193px, 811px 527px, 0 701px);
  }
  .photo {
    position: absolute;
    inset: 0;
    clip-path: polygon(0 701px, 811px 527px, 811px 1200px, 0 1200px);
    background:
      linear-gradient(180deg, rgba(110,4,8,0) 60%, rgba(110,4,8,0.9) 100%),
      radial-gradient(ellipse 22% 18% at 82% 58%, rgba(225,215,215,0.85) 0%, rgba(225,215,215,0) 100%),
      radial-gradient(ellipse 30% 12% at 55% 78%, rgba(25,20,20,0.8) 0%, rgba(25,20,20,0) 100%),
      radial-gradient(ellipse 35% 25% at 88% 90%, rgba(20,16,16,0.9) 0%, rgba(20,16,16,0) 100%),
      linear-gradient(90deg, #a8242a 0%, #b5484c 30%, #8e6a6a 60%, #9c9494 85%, #6e6a6a 100%);
  }
  .headline {
    position: absolute;
    left: 30px;
    top: 388px;
    transform: rotate(-14deg);
    transform-origin: left top;
    margin: 0;
    font-weight: 800;
    line-height: 0.82;
  }
  .headline-small {
    display: block;
    margin-left: 150px;
    font-size: 80px;
    letter-spacing: -1px;
    color: var(--white);
  }
  .headline-large {
    display: block;
    padding-bottom: 0.28em;
    font-size: 240px;
    letter-spacing: -6px;
    color: var(--red);
    background: linear-gradient(180deg, var(--red-bright) 0%, var(--red-mid) 60%, #a80a0a 100%);
    -webkit-background-clip: text;
    background-clip: text;
    -webkit-text-fill-color: transparent;
  }
  .offer {
    position: absolute;
    left: 50px;
    top: 942px;
    margin: 0;
    color: var(--white);
    font-style: italic;
    font-weight: 800;
    line-height: 0.95;
  }
  .offer-line1 { display: block; font-size: 80px; letter-spacing: -2px; }
  .offer-line2 { display: block; font-size: 108px; letter-spacing: -2px; }
</style>
</head>
<body>
  <main class="flyer">
    <div class="photo" role="img" aria-label="Red-tinted photo of a rider leaning over the handlebars of an indoor cycling bike in a spin class"></div>
    <div class="band"></div>

    <header class="brand">
      <span class="brand-mark"></span>
      <span class="brand-name">BoltForge Millbrook Vale</span>
    </header>

    <h1 class="headline">
      <span class="headline-small">Indoor</span>
      <span class="headline-large">Cycling</span>
    </h1>

    <p class="offer">
      <span class="offer-line1">Try a class</span>
      <span class="offer-line2">for FREE!</span>
    </p>
  </main>
</body>
</html>
```